Freeze Dried Raw Dog Food Label

Create a label for a Freeze Dried Raw dog and cat food line.
There are four flavors (beef, bison, fish and chicken).
4 x 8" Label FRONT AND BACK
Please see website www.tolvernfeeds.com for our other product labels that this will need to stand next to.
Please use this color codes for the different flavors:
Chicken: #d5c55c
Beef: 469b9f
Bison: #275e6d
Fish: #a07980
The only other colors that should be used are Black, White, gray scale, and the shiny metallic gold as seen on our website: www.tolvernfeeds.com
There will have 8 Variations:
Beef for dogs
Beef for Cats
Chicken for dogs
Chicken for cats
Bison for dogs
Bison for cats
Fish for dogs
Fish for cats.
There will be (2) 4X8 inch labels for each variation (a front side and a back side)
The Nutritional Information of the 4 flavors, is as follows:
BEEF
Ingredients
Beef, Beef Kidneys, Beef Hearts, Beef Liver, Whole Egg, Flaxseed, Organic Sweet Potato, Kelp, Organic Carrots, Organic Apples, Organic Blueberries, Cod Liver Oil, Pumpkin Seeds, Organic Spinach, Chicory Root, Organic Cranberries, Ginger, Mixed Tocopherols, Inulin, Dried Enterococcus faecium, Fermentation Product, Dried Lactobacillus acidophilus fermentation product
Calorie Content
Kcal/Cup 182
Guaranteed Analysis
Crude Protein – 38% (min)
Crude Fat – 36% (min)
Crude Fiber – 4% (max)
Moisture – 5% (max)
CHICKEN
Ingredients
Chicken, Chicken Liver, Chicken Hearts, Whole Egg, Flaxseed, Organic Sweet Potato, Kelp, Organic Carrots, Organic Apples, Organic Blueberries, Cod Liver Oil, Pumpkin Seeds, Organic Spinach, Chicory Root, Organic Cranberries, Ginger, Mixed Tocopherols, Inulin, Dried Enterococcus faecium, Fermentation Product, Dried Lactobacillus acidophilus fermentation product.
Calorie Content
Kcal/Cup 185
Guaranteed Analysis
Crude Protein – 45% (min)
Crude Fat – 34% (min)
Crude Fiber – 4% (max)
Moisture – 5% (max)
BISON:
Ingredients
Bison, Bison kidneys, Bison Livers, Whole Egg, Flaxseed, Organic Sweet Potato, Kelp, Organic Carrots, Organic Apples, Organic Blueberries, Cod Liver Oil, Pumpkin Seeds, Organic Spinach, Chicory Root, Organic Cranberries, Ginger, Mixed Tocopherols, Inulin, Dried Enterococcus faecium, Fermentation Product, Dried Lactobacillus acidophilus fermentation product.
Calorie Content
Kcal/Cup 186
Guaranteed Analysis
Crude Protein – 32% (min)
Crude Fat – 38% (min)
Crude Fiber – 5% (max)
Moisture – 5% (max)
FISH
Ingredients
Tuna, Salmon, Pollock, Whole Egg, Flaxseed, Organic Sweet Potato, Kelp, Organic Carrots, Organic Apples, Organic Blueberries, Cod Liver Oil, Pumpkin Seeds, Organic Spinach, Chicory Root, Organic Cranberries, Ginger, Mixed Tocopherols, Inulin, Dried Enterococcus faecium, Fermentation Product, Dried Lactobacillus acidophilus fermentation product.
Calorie Content
Kcal/Cup 455, Kcal/oz 114
Guaranteed Analysis
Crude Protein – 40% (min)
Crude Fat – 37% (min)
Crude Fiber – 4% (max)
Moisture – 5% (max)
THINGS TO ADD
Feeding Guidelines: Insert a QR CODE

```html
<!DOCTYPE html>
<html lang="en">
<head>
<meta charset="UTF-8">
<title>Freeze Dried Raw Food Labels</title>
<link href="https://fonts.googleapis.com/css2?family=Bebas+Neue&family=Roboto:wght@400;500&display=swap" rel="stylesheet">
<style>
  :root {
    --chicken: #d5c55c;
    --fish: #a07980;
    --bison: #275e6d;
    --beef: #469b9f;
    --ink: #3a3a3a;
    --rule: #2a2a2a;
    --paper: #ffffff;
    --stage: #f4f4f4;
    --soft-gray: #d9d9d9;
  }
  * { margin: 0; padding: 0; box-sizing: border-box; }
  html, body { width: 1200px; height: 1200px; overflow: hidden; }
  body {
    background: var(--stage);
    font-family: "Roboto", Arial, sans-serif;
    position: relative;
  }
  .label-row {
    position: absolute;
    top: 347px;
    left: 40px;
    display: flex;
    gap: 40px;
  }
  .label {
    position: relative;
    width: 250px;
    height: 505px;
    background: var(--paper);
    box-shadow: 0 2px 10px rgba(0,0,0,0.08);
    overflow: hidden;
  }
  .label--chicken { --flavor: var(--chicken); }
  .label--fish { --flavor: var(--fish); }
  .label--bison { --flavor: var(--bison); }
  .label--beef { --flavor: var(--beef); }

  .tagline {
    position: absolute;
    left: 55px;
    top: 42px;
    width: 78px;
    height: 46px;
    background: linear-gradient(160deg, #e6e6e6, #f2f2f2);
    border-radius: 4px;
  }
  .seal {
    position: absolute;
    left: 44px;
    top: 72px;
    width: 44px;
    height: 44px;
  }
  .ribbon {
    position: absolute;
    top: 0;
    right: 32px;
    width: 34px;
    height: 130px;
    background: var(--flavor);
    clip-path: polygon(0 0, 100% 0, 100% 100%, 50% 92%, 0 100%);
  }
  .ribbon span {
    position: absolute;
    left: 50%;
    top: 58px;
    transform: translate(-50%, -50%) rotate(-90deg);
    white-space: nowrap;
    font-family: "Bebas Neue", sans-serif;
    font-size: 25px;
    letter-spacing: 0.5px;
    color: var(--paper);
  }
  .illustration {
    position: absolute;
    left: 30px;
    top: 150px;
    width: 205px;
    height: 215px;
    border-radius: 40% 45% 30% 35%;
    background: radial-gradient(ellipse at 55% 45%, var(--flavor), transparent 72%);
    opacity: 0.35;
  }
  .title {
    position: absolute;
    left: 32px;
    top: 190px;
    font-family: "Bebas Neue", sans-serif;
    color: var(--ink);
    line-height: 0.88;
  }
  .title .big { display: block; font-size: 56px; letter-spacing: 0.5px; }
  .title .small { display: block; font-size: 45px; margin-top: 8px; letter-spacing: 0.5px; }
  .formula {
    position: absolute;
    left: 0; right: 0;
    top: 380px;
    text-align: center;
    font-family: "Bebas Neue", sans-serif;
    font-size: 26px;
    color: var(--flavor);
  }
  .claims {
    position: absolute;
    left: 35px; right: 35px;
    top: 418px;
    border-top: 2px solid var(--rule);
    border-bottom: 2px solid var(--rule);
    padding: 8px 0 7px;
    text-align: center;
    font-size: 8.5px;
    line-height: 1.3;
    color: var(--rule);
  }
  .net-weight {
    position: absolute;
    left: 0; right: 0;
    top: 478px;
    text-align: center;
    font-size: 8.5px;
    color: var(--rule);
  }
</style>
</head>
<body>
  <main class="label-row">
    <article class="label label--chicken">
      <div class="tagline" role="img" aria-label="Hand-lettered tagline"></div>
      <svg class="seal" viewBox="0 0 44 44" aria-hidden="true"><circle cx="22" cy="22" r="20" fill="none" stroke="#bdbdbd" stroke-width="1.2"/></svg>
      <div class="ribbon"><span>For Dogs</span></div>
      <div class="illustration" role="img" aria-label="Engraved illustration of a chicken"></div>
      <h2 class="title"><span class="big">Freeze<br>Dried</span><span class="small">Raw Food</span></h2>
      <p class="formula">Chicken Formula</p>
      <p class="claims">NATURAL PRODUCT,<br>FREE OF METALS, PESTICIDES, MICROBES</p>
      <p class="net-weight">NET.WT 2LB</p>
    </article>

    <article class="label label--fish">
      <div class="tagline" role="img" aria-label="Hand-lettered tagline"></div>
      <svg class="seal" viewBox="0 0 44 44" aria-hidden="true"><circle cx="22" cy="22" r="20" fill="none" stroke="#bdbdbd" stroke-width="1.2"/></svg>
      <div class="ribbon"><span>For Dogs</span></div>
      <div class="illustration" role="img" aria-label="Engraved illustration of fish swimming over waves"></div>
      <h2 class="title"><span class="big">Freeze<br>Dried</span><span class="small">Raw Food</span></h2>
      <p class="formula">Fish Formula</p>
      <p class="claims">NATURAL PRODUCT,<br>FREE OF METALS, PESTICIDES, MICROBES</p>
      <p class="net-weight">NET.WT 2LB</p>
    </article>

    <article class="label label--bison">
      <div class="tagline" role="img" aria-label="Hand-lettered tagline"></div>
      <svg class="seal" viewBox="0 0 44 44" aria-hidden="true"><circle cx="22" cy="22" r="20" fill="none" stroke="#bdbdbd" stroke-width="1.2"/></svg>
      <div class="ribbon"><span>For Dogs</span></div>
      <div class="illustration" role="img" aria-label="Engraved illustration of a bison"></div>
      <h2 class="title"><span class="big">Freeze<br>Dried</span><span class="small">Raw Food</span></h2>
      <p class="formula">Bison Formula</p>
      <p class="claims">NATURAL PRODUCT,<br>FREE OF METALS, PESTICIDES, MICROBES</p>
      <p class="net-weight">NET.WT 2LB</p>
    </article>

    <article class="label label--beef">
      <div class="tagline" role="img" aria-label="Hand-lettered tagline"></div>
      <svg class="seal" viewBox="0 0 44 44" aria-hidden="true"><circle cx="22" cy="22" r="20" fill="none" stroke="#bdbdbd" stroke-width="1.2"/></svg>
      <div class="ribbon"><span>For Dogs</span></div>
      <div class="illustration" role="img" aria-label="Engraved illustration of a cow"></div>
      <h2 class="title"><span class="big">Freeze<br>Dried</span><span class="small">Raw Food</span></h2>
      <p class="formula">Beef Formula</p>
      <p class="claims">NATURAL PRODUCT,<br>FREE OF METALS, PESTICIDES, MICROBES</p>
      <p class="net-weight">NET.WT 2LB</p>
    </article>
  </main>
</body>
</html>
```